Brell Harbor Company Business Cards

Front and Back Business Card - logo and text setup - cool design. I need workable photoshop or illustrator files so I can setup each employee card with design that is created
Updates

Hi everyone, thank you for the great entries. Please no more white and blue cards - there are so many already - black and silver only now please. thanks!

Target Market(s)

Construction Industry - Facility Managers

Industry/Entity Type

Construction

Contact Information for Business Card

I really like contemporary simplistic looks - clean neat....not opposed to seeing some black backrounds

Requirements
Must have
• Logo/website address with design on front only - www.brellharbor-example.com (logo attached)
• Back:
• Name/Title/Company Address/Phone/email address
Nice to have
• Cool design
Should not have
• Nothing gimmicky like Fire or Water - since we are a Fire Protection company - it has all been done

```html
<!DOCTYPE html>
<html lang="en">
<head>
<meta charset="utf-8">
<title>Brell Harbor Company Business Cards</title>
<link href="https://fonts.googleapis.com/css2?family=Lato:wght@400;700;900&display=swap" rel="stylesheet">
<style>
  :root {
    --backdrop: #3a3a3a;
    --black: #141414;
    --black-soft: #222325;
    --silver: #c4c7cc;
    --silver-light: #eceef0;
    --silver-mid: #9a9da3;
    --white: #ffffff;
    --ink: #1c1c1c;
  }
  * { margin: 0; padding: 0; box-sizing: border-box; }
  html, body {
    width: 1200px; height: 900px; overflow: hidden;
    background: var(--backdrop);
    font-family: "Lato", sans-serif;
  }
  .card {
    position: absolute;
    width: 620px; height: 354px;
    box-shadow: 0 10px 30px rgba(0,0,0,0.5);
    overflow: hidden;
  }
  /* Front */
  .card-front { left: 80px; top: 70px; background: var(--black); }
  .card-front .brand-name {
    position: absolute; left: 0; right: 0; top: 128px;
    text-align: center; color: var(--silver);
    font-weight: 900; font-size: 64px; letter-spacing: -1px;
  }
  .card-front .web {
    position: absolute; left: 0; right: 0; bottom: 42px;
    text-align: center; color: var(--silver);
    font-size: 15px; letter-spacing: 0.5px;
  }
  /* Back */
  .card-back { left: 500px; top: 470px; background: var(--silver-light); }
  .card-back .brand-name {
    position: absolute; left: 38px; top: 92px;
    color: var(--black); font-weight: 900; font-size: 46px; letter-spacing: -1px;
  }
  .person { position: absolute; right: 40px; top: 100px; text-align: right; }
  .person .name { color: var(--black); font-weight: 700; font-size: 24px; }
  .person .title { color: var(--silver-mid); font-size: 14px; margin-top: 2px; }
  .divider {
    position: absolute; left: 38px; right: 40px; top: 168px;
    height: 1px; background: var(--black-soft);
  }
  .contact { position: absolute; left: 44px; top: 196px; color: var(--ink); font-size: 15px; }
  .contact li { list-style: none; display: flex; align-items: center; gap: 10px; margin-bottom: 6px; }
  .contact svg { width: 14px; height: 14px; }
  .address {
    position: absolute; right: 40px; top: 194px;
    text-align: right; color: var(--ink); font-size: 15px; line-height: 1.35;
  }
  .footer-band { position: absolute; left: 0; bottom: 0; width: 620px; height: 90px; }
  .footer-band .web {
    position: absolute; right: 28px; bottom: 14px;
    color: var(--silver); font-size: 13px; letter-spacing: 0.4px;
  }
</style>
</head>
<body>

<section class="card card-front" aria-label="Business card front">
  <div class="brand-name">Brell Harbor</div>
  <div class="web">www.brellharbor-example.com</div>
</section>

<section class="card card-back" aria-label="Business card back">
  <div class="brand-name">Brell Harbor</div>

  <div class="person">
    <div class="name">Maren Voss Calder</div>
    <div class="title">President</div>
  </div>

  <div class="divider"></div>

  <ul class="contact">
    <li>
      <svg viewBox="0 0 24 24" aria-hidden="true"><path fill="#141414" d="M6.6 10.8c1.4 2.8 3.8 5.1 6.6 6.6l2.2-2.2c.3-.3.7-.4 1-.2 1.1.4 2.3.6 3.6.6.6 0 1 .4 1 1V20c0 .6-.4 1-1 1C10.6 21 3 13.4 3 4c0-.6.4-1 1-1h3.5c.6 0 1 .4 1 1 0 1.3.2 2.5.6 3.6.1.3 0 .7-.2 1z"/></svg>
      (555) 014-2273
    </li>
    <li>
      <svg viewBox="0 0 24 24" aria-hidden="true"><path d="M2 5h20v14H2z M3 6l9 7 9-7" fill="none" stroke="#141414" stroke-width="2"/></svg>
      info@brellharbor-example.com
    </li>
  </ul>

  <div class="address">
    48 Quarry Lane<br>
    Westfield Bay, NY 10099
  </div>

  <div class="footer-band">
    <svg width="620" height="90" viewBox="0 0 620 90" aria-hidden="true">
      <path d="M0 62 L360 62 C380 62 385 52 395 46 L0 46 Z" fill="var(--silver-mid)"/>
      <path d="M0 70 L370 70 C400 70 410 30 450 24 L620 24 L620 90 L0 90 Z" fill="var(--black)"/>
    </svg>
    <div class="web">www.brellharbor-example.com</div>
  </div>
</section>

</body>
</html>
```